Cardiology Practice needs a Heart Scan Order Form

Busy cardiology practice needs an order form for a heart scan test. Sample is attached. One side should have all information noted and the other side should have our physician names (Dorian Velko, MD, L.N. Morvesti, MD, Ovila Brandt, MD, Tomas Velko, MD, and Gerald Pompetti, MD. It should have the map that is uploaded and our demographic information (Crestfield Cardiac PLLC, 712 Harrow Ln. Ste. K, Melrick, TX 77431 along with phone 832-417-2286 and fax 832-417-2287) as well as our web address (crestfieldcardiac.example). Our primary colors are red, black and white. Needs to fit paper size 8 1/2 by 11.

Target Market(s)

Healthcare

Industry/Entity Type

Health Care

Font styles to use
Serif

Colors
ec1f27

Requirements
Must have
• Logo, information listed on sample form, demographics and physician names as well as website.
Nice to have
• Open to suggestions
Should not have
• Physician Pictures

```html
<!DOCTYPE html>
<html lang="en">
<head>
<meta charset="utf-8">
<title>Crestfield Cardiac – Calcium Score Heart Scan Order Form</title>
<link href="https://fonts.googleapis.com/css2?family=Source+Sans+3:wght@400;600;700;800&display=swap" rel="stylesheet">
<style>
:root{
  --red:#be1e2d;
  --black:#0d0d0d;
  --white:#ffffff;
  --grey-bg:#929396;
  --band:#e6e6e6;
  --bar-dark:#58595b;
  --ink:#231f20;
  --map:#eceae4;
}
*{box-sizing:border-box;margin:0;padding:0}
html,body{width:1200px;height:793px;overflow:hidden;background:var(--grey-bg);font-family:"Source Sans 3",sans-serif;color:var(--ink)}
.sheet{position:absolute;top:98px;width:474px;height:613px;background:var(--white);box-shadow:2px 3px 6px rgba(0,0,0,.35);overflow:hidden}
.sheet--order{left:99px}
.sheet--info{left:630px}
.t{position:absolute;white-space:nowrap;font-size:6.4px;line-height:1}
.header-art{position:absolute;left:0;top:0}
.brand{position:absolute;left:20px;top:30px;display:flex;align-items:center;gap:6px;color:var(--white);font-weight:800;font-size:15px;letter-spacing:.5px}
.brand-dot{width:10px;height:10px;border-radius:50%;background:var(--white)}
.title{position:absolute;right:26px;top:16px;color:var(--white);font-weight:800;font-size:18.5px;letter-spacing:-.2px}
.line{position:absolute;height:0;border-top:.7px solid var(--ink)}
.schedule .t{color:var(--ink)}
.doctor-bar{position:absolute;left:15px;top:113px;width:434px;height:23px;background:var(--red);border-radius:7px 7px 0 0;display:flex;align-items:center;justify-content:center;gap:7px;color:var(--white);font-weight:700;font-size:7px}
.band{position:absolute;height:10px;background:var(--band);font-weight:700;font-size:6.4px;line-height:10px;padding-left:3px}
.box{position:absolute;width:5px;height:5px;border:.7px solid var(--ink)}
.sexbox{position:absolute;height:8px;border:.7px solid var(--ink);font-size:6px;line-height:7px;text-align:center}
.note-bar{position:absolute;left:14px;top:337px;width:434px;height:11px;background:var(--bar-dark);color:var(--white);font-size:6.4px;line-height:11px;padding-left:15px}
.rules{position:absolute;left:25px;top:360px;width:420px;list-style:none;font-size:6.2px;line-height:7.6px}
.rules li{position:relative;padding-left:13px;margin-bottom:3px}
.rules li::before{content:"";position:absolute;left:1px;top:1px;width:4px;height:4px;border:.7px solid var(--ink)}
.rules u{text-decoration:underline}
.ack{position:absolute;left:21px;top:474px;width:430px;font-size:6.4px;line-height:8.4px}
.sig-label{text-align:center;width:116px}
.ref-box{position:absolute;left:311px;top:498px;width:137px;height:63px;border:.8px solid var(--ink)}
.ref-head{background:var(--bar-dark);color:var(--white);font-size:6.4px;height:10px;line-height:10px;padding-left:5px}
.ref-row{height:17.5px;border-bottom:.7px solid var(--ink);font-size:4.4px;padding:7px 0 0 5px}
.ref-row:last-child{border-bottom:0}
.footer-art{position:absolute;left:0;bottom:0}
.foot-name{position:absolute;left:13px;top:583px;color:var(--red);font-weight:700;font-size:7.5px}
.foot-visit{position:absolute;left:13px;top:594px;color:var(--white);font-size:6.2px}
.foot-contact{position:absolute;right:26px;top:599px;display:flex;gap:8px;color:var(--white);font-size:6.6px;align-items:center}
.foot-contact span{display:flex;align-items:center;gap:3px}
.address-bar{position:absolute;left:14px;top:113px;width:435px;height:23px;background:var(--red);border-radius:7px 7px 0 0;display:flex;align-items:center;justify-content:center;gap:8px;color:var(--white);font-weight:700;font-size:11px}
.map{position:absolute;left:17px;top:136px;width:432px;height:254px;background:linear-gradient(135deg,#efece4 0%,#f4f1e8 45%,#e7e5e0 100%)}
.tab{position:absolute;left:17px;height:20px;color:var(--white);font-weight:700;font-size:8.5px;line-height:20px;padding-left:12px;background:var(--red);clip-path:polygon(0 0,88% 0,100% 100%,0 100%)}
.staff{position:absolute;left:17px;width:432px;background:var(--band);display:flex;align-items:center;padding-left:12px;gap:7px;font-weight:600;font-size:7.2px}
</style>
</head>
<body>

<!-- Order form side -->
<section class="sheet sheet--order">
  <svg class="header-art" width="474" height="84" viewBox="0 0 474 84">
    <path d="M0 0H474V47H300C262 47 256 82 205 82H0Z" fill="var(--red)"/>
    <path d="M172 0H474V47H236C206 47 200 0 172 0Z" fill="var(--black)"/>
  </svg>
  <div class="brand"><span class="brand-dot"></span>CRESTFIELD CARDIAC</div>
  <div class="title">CALCIUM SCORE HEART SCAN</div>

  <div class="schedule">
    <div class="t" style="left:288px;top:54px;color:var(--red)">Test schedule</div>
    <div class="line" style="left:287px;top:62px;width:161px"></div>
    <div class="t" style="left:289px;top:65px">Date:</div>
    <div class="line" style="left:287px;top:73px;width:161px"></div>
    <div class="t" style="left:289px;top:76px">Time:</div>
    <div class="line" style="left:287px;top:85px;width:161px"></div>
  </div>

  <div class="doctor-bar">
    <span>Dorian Velko, M.D.</span>|<span>L.N. Morvesti, M.D.</span>|<span>Ovila Brandt, M.D.</span>|<span>Tomas Velko, M.D.</span>|<span>Gerald Pompetti, M.D.</span>
  </div>

  <div class="band" style="left:13px;top:140px;width:198px">Patient information</div>
  <div class="band" style="left:251px;top:140px;width:197px">Contact information</div>

  <div class="t" style="left:15px;top:158px">Last name</div>
  <div class="t" style="left:95px;top:158px">First name</div>
  <div class="t" style="left:175px;top:158px">MI</div>
  <div class="line" style="left:15px;top:178px;width:196px"></div>
  <div class="t" style="left:254px;top:158px">Address</div>
  <div class="line" style="left:252px;top:178px;width:196px"></div>

  <div class="t" style="left:15px;top:192px">Date of birth</div>
  <div class="line" style="left:15px;top:211px;width:78px"></div>
  <div class="t" style="left:130px;top:192px">Account no.</div>
  <div class="line" style="left:127px;top:211px;width:81px"></div>
  <div class="t" style="left:252px;top:192px">Home phone no.</div>
  <div class="line" style="left:252px;top:211px;width:79px"></div>
  <div class="t" style="left:370px;top:192px">Mobile phone no.</div>
  <div class="line" style="left:368px;top:211px;width:80px"></div>

  <div class="band" style="left:13px;top:219px;width:435px;text-align:center;font-weight:400">Medical information</div>

  <div class="t" style="left:15px;top:234px">Sex:</div>
  <div class="sexbox" style="left:36px;top:233px;width:18px">F</div>
  <div class="sexbox" style="left:64px;top:233px;width:18px">M</div>
  <div class="t" style="left:102px;top:234px">Height:</div>
  <div class="line" style="left:128px;top:241px;width:60px"></div>
  <div class="t" style="left:201px;top:234px">Weight:</div>
  <div class="line" style="left:229px;top:241px;width:60px"></div>
  <div class="t" style="left:309px;top:234px">Race:</div>
  <div class="line" style="left:328px;top:241px;width:120px"></div>

  <div class="t" style="left:14px;top:256px">Diagnosis:</div>
  <div class="line" style="left:51px;top:264px;width:397px"></div>

  <div class="box" style="left:19px;top:279px"></div><div class="t" style="left:33px;top:279px">PCI &nbsp;&nbsp; (no. of stents:______________)</div>
  <div class="box" style="left:140px;top:279px"></div><div class="t" style="left:148px;top:279px">CABG (no. of vessels: ____________)</div>
  <div class="box" style="left:268px;top:279px"></div><div class="t" style="left:280px;top:279px">MI &nbsp;(last event: ______________________)</div>
  <div class="box" style="left:397px;top:279px"></div><div class="t" style="left:408px;top:279px">PCM/ICD</div>

  <div class="box" style="left:19px;top:298px"></div><div class="t" style="left:33px;top:298px">Diabetes</div>
  <div class="box" style="left:95px;top:298px"></div><div class="t" style="left:111px;top:298px">Claustrophobia</div>
  <div class="box" style="left:196px;top:298px"></div><div class="t" style="left:213px;top:298px">Asthma</div>
  <div class="box" style="left:276px;top:298px"></div><div class="t" style="left:294px;top:298px">Emphysema</div>
  <div class="box" style="left:374px;top:298px"></div><div class="t" style="left:392px;top:298px">COPD</div>

  <div class="t" style="left:14px;top:314px">LMP:</div>
  <div class="line" style="left:32px;top:322px;width:77px"></div>
  <div class="box" style="left:117px;top:314px"></div><div class="t" style="left:130px;top:314px">bHCG</div>
  <div class="box" style="left:176px;top:314px"></div><div class="t" style="left:190px;top:314px">Tubal ligation</div>
  <div class="box" style="left:258px;top:314px"></div><div class="t" style="left:272px;top:314px">Post-menopause &gt; 1 year</div>
  <div class="box" style="left:375px;top:314px"></div><div class="t" style="left:389px;top:314px">Hysterectomy</div>

  <div class="note-bar">Please read the following instructions carefully. You might be rescheduled if any of the following instructions are not met.</div>

  <ul class="rules">
    <li>AVOID &nbsp; caffeine containing products (coffee, tea, soda, chocolate, energy drinks, or some over the counter medications)<br>for 4 hours prior to testing.</li>
    <li>AVOID &nbsp; smoking for 4 hours prior to testing.</li>
    <li>AVOID &nbsp; eating or drinking anything except water for 4 hours prior to testing.</li>
    <li>Arrive <u>15 minutes early</u> for your appointment time.</li>
    <li>Wear comfortable clothing. <u>Remove any metal objects,</u> such as jewelry or piercings. Women will be asked to remove bras<br>containing metal underwire.</li>
    <li>Inform your physician or the staff if you are claustrophobic or have a problem staying in restricted environments for any<br>length of time.</li>
    <li>Inform the physician or the staff if you are or think you might be pregnant.</li>
  </ul>

  <p class="ack">I hereby acknowledge that the instructions and procedures pertinent to this study were explained thoroughly, I had time to ask questions, and these questions were addressed satisfactorily.</p>

  <div class="line" style="left:13px;top:507px;width:116px"></div>
  <div class="t sig-label" style="left:13px;top:510px">Patient's print name</div>
  <div class="line" style="left:168px;top:507px;width:121px"></div>
  <div class="t sig-label" style="left:171px;top:510px">Patient's signature</div>
  <div class="line" style="left:13px;top:541px;width:116px"></div>
  <div class="t sig-label" style="left:13px;top:544px">Prescriber's print name</div>
  <div class="line" style="left:168px;top:541px;width:121px"></div>
  <div class="t sig-label" style="left:171px;top:544px">Prescriber's signature</div>

  <div class="ref-box">
    <div class="ref-head">Referring physician contact information</div>
    <div class="ref-row">Order date:</div>
    <div class="ref-row">Tel no.:</div>
    <div class="ref-row">Fax no.:</div>
  </div>

  <svg class="footer-art" width="474" height="44" viewBox="0 0 474 44">
    <path d="M0 0H240C260 0 266 22 278 22V44H0Z" fill="var(--black)"/>
    <path d="M195 44C205 30 212 22 230 22H474V44Z" fill="var(--red)"/>
  </svg>
  <div class="foot-name">Crestfield Cardiac, PLLC.</div>
  <div class="foot-visit">Visit us at 712 Harrow Ln., Ste. K, Melrick, TX 77431.</div>
  <div class="foot-contact">
    <span><svg width="6" height="6" viewBox="0 0 10 10"><path d="M2 0L4 3 3 4.5C4 6.5 5.5 7 6 7L7 6 10 8 8.5 10C4 10 0 6 0 1.5Z" fill="#fff"/></svg>(832) 417-2286</span>
    <span><svg width="6" height="6" viewBox="0 0 10 10"><rect x="1" y="3" width="8" height="5" fill="#fff"/><rect x="3" y="0" width="4" height="3" fill="#fff"/></svg>(832) 417-2287</span>
    <span><svg width="6" height="6" viewBox="0 0 10 10"><circle cx="5" cy="5" r="4.3" fill="none" stroke="#fff"/><path d="M1 5H9M5 1V9" stroke="#fff" stroke-width=".8"/></svg>www.crestfieldcardiac.example</span>
  </div>
</section>

<!-- Information side -->
<section class="sheet sheet--info">
  <svg class="header-art" width="474" height="84" viewBox="0 0 474 84">
    <path d="M0 0H474V47H340C300 47 300 82 245 82H0Z" fill="var(--red)"/>
    <path d="M176 0H474V47H240C210 47 204 0 176 0Z" fill="var(--black)"/>
  </svg>
  <div class="brand"><span class="brand-dot"></span>CRESTFIELD CARDIAC</div>
  <div class="title">CALCIUM SCORE HEART SCAN</div>

  <div class="address-bar">
    <span>Crestfield Cardiac, PLLC.</span>
    <span style="display:flex;align-items:center;gap:4px"><svg width="7" height="10" viewBox="0 0 10 14"><path d="M5 0C2.2 0 0 2.2 0 5c0 3.8 5 9 5 9s5-5.2 5-9C10 2.2 7.8 0 5 0z" fill="var(--black)"/><circle cx="5" cy="5" r="2" fill="var(--red)"/></svg>712 Harrow Ln. Ste. K Melrick, TX 77431</span>
  </div>

  <div class="map" role="img" aria-label="Street map showing the practice location on Harrow Lane in Melrick, with nearby roads and landmarks"></div>

  <div class="tab" style="top:411px;width:138px">Our physicians:</div>
  <div class="staff" style="top:431px;height:29px">
    <span>Dorian Velko, M.D.</span>|<span>L.N. Morvesti, M.D.</span>|<span>Ovila Brandt, M.D.</span>|<span>Tomas Velko, M.D.</span>|<span>Gerald Pompetti, M.D.</span>
  </div>

  <div class="tab" style="top:476px;width:138px">Our nurse practitioners:</div>
  <div class="staff" style="top:496px;height:30px">
    <span>Marla Venholt, MSN, ACNP-BC.</span>|<span>Janelle Ostrow, MSN, APRN, AGNP-C.</span>|<span>Renata Albee, MSN, APRN, NP-C.</span>
  </div>

  <svg class="footer-art" width="474" height="44" viewBox="0 0 474 44">
    <path d="M0 0H240C260 0 266 22 278 22V44H0Z" fill="var(--black)"/>
    <path d="M195 44C205 30 212 22 230 22H474V44Z" fill="var(--red)"/>
  </svg>
  <div class="foot-name">Crestfield Cardiac, PLLC.</div>
  <div class="foot-visit">Visit us at 712 Harrow Ln., Ste. K, Melrick, TX 77431.</div>
  <div class="foot-contact">
    <span><svg width="6" height="6" viewBox="0 0 10 10"><path d="M2 0L4 3 3 4.5C4 6.5 5.5 7 6 7L7 6 10 8 8.5 10C4 10 0 6 0 1.5Z" fill="#fff"/></svg>(832) 417-2286</span>
    <span><svg width="6" height="6" viewBox="0 0 10 10"><rect x="1" y="3" width="8" height="5" fill="#fff"/><rect x="3" y="0" width="4" height="3" fill="#fff"/></svg>(832) 417-2287</span>
    <span><svg width="6" height="6" viewBox="0 0 10 10"><circle cx="5" cy="5" r="4.3" fill="none" stroke="#fff"/><path d="M1 5H9M5 1V9" stroke="#fff" stroke-width=".8"/></svg>www.crestfieldcardiac.example</span>
  </div>
</section>

</body>
</html>
```